WordPress Site Design and Code for Technology Consulting Startup

We need a WordPress design and code to a new site on Nimbo Vault. We have the logo and colors ready. The site will be a brochure site with a CONTACT page that contains a form that the prospective client fills out. The other pages would be ABOUT / SERVICES (3 option drop-down) / SUPPORT. The site should be appropriate for an IT Consulting / IT Managed Services / IT Project Management services in the Chicago area.

Target Market(s)

Across small, medium, large businesses.

Industry/Entity Type

Technology, network infrastructure, IT.

Coding

Coded - Design and coding required

Number of Pages Required

5+ page

Requirements
Nice to have
• I prefer mid-modern / simple / art deco / minimalist.

```html
<!DOCTYPE html>
<html lang="en">
<head>
<meta charset="utf-8">
<title>Velorin — IT Consulting</title>
<link rel="stylesheet" href="https://fonts.googleapis.com/css2?family=Michroma&family=Poppins:wght@400;500;600&family=Lato:wght@400&display=swap">
<style>
:root{
  --teal:#1f93ad;
  --teal-light:#2ea6bf;
  --orange:#f47b20;
  --ink:#1b1b1b;
  --text:#333;
  --field:#e4e4e4;
  --white:#fff;
  --cream:#fdf3ea;
}
*{box-sizing:border-box;margin:0;padding:0}
html,body{width:1200px;height:3423px;overflow:hidden;background:var(--white)}
body{position:relative;font-family:"Poppins",sans-serif;color:var(--text)}
.display{font-family:"Michroma",sans-serif;text-transform:uppercase;letter-spacing:1px}
.btn{display:inline-block;background:var(--orange);color:var(--white);font-family:"Michroma",sans-serif;font-size:15px;letter-spacing:1.5px;text-transform:uppercase;text-align:center;line-height:53px;height:53px;width:209px}
.btn-small{font-family:"Poppins",sans-serif;font-weight:600;font-size:16px;letter-spacing:.3px;width:143px;height:46px;line-height:46px}
/* header */
.site-header{position:absolute;left:0;top:0;width:1200px;height:80px;border-bottom:1px solid #ddd;background:var(--white)}
.brand{position:absolute;left:75px;top:20px;display:flex;align-items:center;gap:10px;font-family:"Michroma",sans-serif;font-size:27px;color:var(--teal)}
.brand-mark{width:36px;height:36px;background:var(--orange)}
.main-nav{position:absolute;right:75px;top:33px;display:flex;gap:46px;font-family:"Michroma",sans-serif;font-size:13px;color:var(--ink)}
.main-nav .current{color:var(--teal)}
/* hero */
.hero{position:absolute;left:0;top:80px;width:1200px;height:659px;background:radial-gradient(circle at 38% 40%,#b8731e 0,#5a3a17 14%,#0c1a2c 38%,#0a1322 70%,#07101c 100%)}
.hero-copy{position:absolute;right:75px;top:190px;text-align:right;color:var(--white)}
.hero-copy h1{font-size:60px;line-height:68px;font-weight:400}
.hero-copy p{font-size:23px;line-height:34px;margin:10px 0 20px}
.dots{position:absolute;left:562px;top:600px;display:flex;gap:11px}
.dots span{width:13px;height:13px;border-radius:50%;background:var(--white)}
.dots span:first-child{background:var(--teal)}
/* about */
.about-tint{position:absolute;left:0;top:817px;width:434px;height:588px;background:linear-gradient(90deg,#eef6f8,var(--cream))}
.about-copy{position:absolute;left:75px;top:812px;width:330px}
.about-copy h2{font-size:43px;line-height:50px;color:var(--ink);font-weight:400}
.about-copy h2 span{color:var(--teal)}
.about-copy p{font-size:15px;line-height:27.6px;margin-top:26px;color:var(--text)}
.about-copy p+p{margin-top:8px}
.about-copy .btn{margin-top:40px}
.about-media{position:absolute;left:434px;top:817px;width:766px;height:588px;background:radial-gradient(circle at 48% 38%,#5fc8f5 0,#1c6fb8 20%,#123f73 48%,#0e2a4f 100%)}
.about-media .brand-overlay{position:absolute;left:290px;top:430px;font-family:"Michroma",sans-serif;font-size:30px;color:var(--ink)}
/* services */
.services{position:absolute;left:0;top:1500px;width:1200px;height:730px}
.services svg{position:absolute;left:0;top:0}
.services h2{position:absolute;left:0;top:118px;width:1200px;text-align:center;color:var(--white);font-size:43px;font-weight:400}
.service{position:absolute;top:222px;width:340px;text-align:center;color:var(--white)}
.service svg{position:static;display:block;margin:0 auto}
.service h3{font-family:"Michroma",sans-serif;font-weight:400;font-size:20px;line-height:27px;margin-top:24px;text-transform:uppercase;letter-spacing:1px}
.service p{font-size:17.5px;line-height:31px;margin:10px 0 28px}
.divider{position:absolute;top:210px;width:1px;height:390px;background:rgba(255,255,255,.7)}
/* support */
.support{position:absolute;left:75px;top:2166px;width:1052px;height:432px}
.support svg{position:absolute;left:0;top:0}
.support-copy{position:absolute;left:0;top:82px;width:1052px;text-align:center;color:var(--white)}
.support-copy h2{font-size:43px;font-weight:400}
.support-copy p{font-size:15px;line-height:30px;width:860px;margin:18px auto 28px}
/* contact */
.contact-tint{position:absolute;left:767px;top:2665px;width:433px;height:632px;background:linear-gradient(160deg,#e7f2f5,#f5fafb)}
.contact-photo{position:absolute;left:0;top:2665px;width:767px;height:587px;background:linear-gradient(135deg,#8d8370,#6c5d4d 45%,#4a5a6a 75%,#8a7460)}
.contact-card{position:absolute;left:615px;top:2731px;width:512px;height:454px;background:var(--white);padding:40px 0 0 37px}
.contact-card h2{font-size:43px;font-weight:400;color:var(--ink)}
.contact-card h2 span{color:var(--teal)}
.form{display:grid;grid-template-columns:230px 230px;gap:12px;margin-top:24px}
.field{background:var(--field);height:53px;font-family:"Lato",sans-serif;font-size:16px;color:#222;padding:17px 20px}
.field.wide{grid-column:1/3;height:106px;padding-top:14px}
.form .btn{margin-top:1px}
/* footer */
.site-footer{position:absolute;left:0;top:3313px;width:1200px;height:110px;background:var(--teal);color:var(--white)}
.copyright{position:absolute;left:75px;top:47px;font-size:13.5px}
.footer-brand{position:absolute;left:0;width:1200px;top:38px;text-align:center;font-family:"Michroma",sans-serif;font-size:24px}
.follow{position:absolute;left:933px;top:28px;font-family:"Michroma",sans-serif;font-size:14px;letter-spacing:1px}
.social{position:absolute;left:933px;top:62px;display:flex;gap:21px}
.social span{width:24px;height:24px;border-radius:50%;background:var(--white)}
</style>
</head>
<body>

<header class="site-header">
  <div class="brand"><span class="brand-mark"></span>VELORIN</div>
  <nav class="main-nav">
    <span class="current">Home</span><span>About Us</span><span>Services</span><span>Support</span><span>Contact Us</span>
  </nav>
</header>

<section class="hero" role="img" aria-label="Hand touching a glowing network of connected points on a dark background">
  <div class="hero-copy">
    <h1 class="display">Welcome to<br>Velorin</h1>
    <p>Sed ut perspiciatis unde omnis iste natus error sit<br>voluptatem accusantiumdoloremque.</p>
    <span class="btn">Read More</span>
  </div>
  <div class="dots"><span></span><span></span><span></span><span></span></div>
</section>

<div class="about-tint"></div>
<section class="about-copy">
  <h2 class="display">About<br><span>Velorin</span></h2>
  <p>Sed ut perspiciatis unde omnis iste natus error sit voluptatem accusantium doloremque laudantium, totam rem aperiam, eaque ipsa quae ab illo inventore veritatis et quasi architecto beatae vitae dicta sunt explicaboemo enim ipsam voluptatem quia voluptas sit aspernatur aut odit aut fugit, sed quia consequuntur magni dolores eos qui ratione voluptatem sequi nesciunt.</p>
  <p>Neque porro quisquam est, qui dolorem ipsum quia dolor sit amet, consectetur, adipisci velit, sed quia non numquam eius modi tempora incidunt ut labore</p>
  <span class="btn">Read More</span>
</section>
<div class="about-media" role="img" aria-label="Open hand holding a glowing digital globe">
  <div class="brand-overlay">VELORIN</div>
</div>

<section class="services">
  <svg width="1200" height="730" viewBox="0 0 1200 730">
    <path d="M0 140 Q600 -120 1200 140 L1200 730 L0 730 Z" fill="var(--teal)"/>
    <path d="M100 110 L100 700 L320 700 L320 360 Z" fill="#2a9fb8" opacity=".5"/>
    <path d="M880 110 L880 700 L1100 700 L1100 110 Z" fill="#2a9fb8" opacity=".4"/>
  </svg>
  <h2 class="display">Our Services</h2>
  <div class="divider" style="left:420px"></div>
  <div class="divider" style="left:780px"></div>

  <div class="service" style="left:64px">
    <svg width="72" height="72" viewBox="0 0 72 72" fill="none" stroke="#fff" stroke-width="2"><circle cx="36" cy="20" r="10"/><circle cx="16" cy="46" r="6"/><circle cx="56" cy="46" r="6"/><path d="M6 70v-8a10 10 0 0 1 20 0v8M46 70v-8a10 10 0 0 1 20 0v8M30 30v10h12V30"/></svg>
    <h3>IT Consulting</h3>
    <p>Nemo enim ipsam voluptatem quia voluptas sit aspernatur aut odit aut fugit, sed quia consequuntur magni dolores eos.</p>
    <span class="btn btn-small">LEARN MORE</span>
  </div>

  <div class="service" style="left:430px">
    <svg width="72" height="72" viewBox="0 0 72 72" fill="none" stroke="#fff" stroke-width="2"><rect x="4" y="14" width="64" height="40"/><path d="M26 66h20M36 54v12"/><circle cx="48" cy="18" r="11"/><circle cx="48" cy="18" r="4"/></svg>
    <h3>IT Managed<br>Services</h3>
    <p>Nemo enim ipsam voluptatem quia voluptas sit aspernatur aut odit aut fugit, sed quia con.</p>
    <span class="btn btn-small">LEARN MORE</span>
  </div>

  <div class="service" style="left:792px">
    <svg width="72" height="72" viewBox="0 0 72 72" fill="none" stroke="#fff" stroke-width="2"><rect x="6" y="2" width="46" height="66"/><path d="M12 12h34M12 24h20M12 34h30M12 44h24"/><circle cx="56" cy="56" r="10"/><circle cx="56" cy="56" r="4"/></svg>
    <h3>IT Project<br>Management<br>Services</h3>
    <p>Nemo enim ipsam voluptatem quia voluptas sit aspernatur aut odit aut fugit, sed quia con.</p>
    <span class="btn btn-small">LEARN MORE</span>
  </div>
</section>

<section class="support">
  <svg width="1052" height="432" viewBox="0 0 1052 432" role="img" aria-label="Smiling support agent with a headset in a bright office">
    <defs><linearGradient id="supportTone" x1="0" y1="0" x2="1" y2="0"><stop offset="0" stop-color="#5a5a5a"/><stop offset=".45" stop-color="#4a3a38"/><stop offset="1" stop-color="#3e3e42"/></linearGradient></defs>
    <path d="M0 0 H1052 V312 Q526 520 0 312 Z" fill="url(#supportTone)"/>
  </svg>
  <div class="support-copy">
    <h2 class="display">Support</h2>
    <p>Sed ut perspiciatis unde omnis iste natus error sit voluptatem accusantium doloremque laudantium, totam rem&nbsp; aperiam, eaque ipsa quae ab illo inventore veritatis et quasi architecto beatae vitae dicta sunt explicaboemo enimipsam voluptatem quia voluptas sit aspernatur aut odit.</p>
    <span class="btn">Read More</span>
  </div>
</section>

<div class="contact-tint"></div>
<div class="contact-photo" role="img" aria-label="Man with glasses working on a laptop at a wooden desk"></div>
<section class="contact-card">
  <h2 class="display">Contact <span>Us</span></h2>
  <div class="form">
    <div class="field">Name</div>
    <div class="field">Email Address</div>
    <div class="field">Phone No</div>
    <div class="field">Subject</div>
    <div class="field wide">Message</div>
    <span class="btn">Submit</span>
  </div>
</section>

<footer class="site-footer">
  <div class="copyright">Copyright © 2023 Velorin All Right Reserved</div>
  <div class="footer-brand">VELORIN</div>
  <div class="follow">FOLLOW US</div>
  <div class="social"><span></span><span></span><span></span><span></span><span></span></div>
</footer>

</body>
</html>
```